Business cards for Harbourline Supply Pty Ltd that import building products into Australia from China
Target Market(s)
Business to Business
Industry/Entity Type
Business
Contact Information for Business Card
Front: Logo and Business Name
Rear:
Vernon Ashcombe
General Manager
Mobile: 0427 619 354
email: vern@harbourlinesupply.com.au
alternative email: vern@coastwardgoods.com.au
web: www.harbourlinesupply.com.au
Adelaide, Brisbane and Darwin
Colors
ec1f27
fbee3d

```html
<!DOCTYPE html>
<html lang="en">
<head>
<meta charset="utf-8">
<title>Harbourline Supply Pty Ltd – Business Cards</title>
<link href="https://fonts.googleapis.com/css2?family=Lato:wght@400;700&display=swap" rel="stylesheet">
<style>
  :root {
    --brand-red: #ec1f27;
    --brand-yellow: #fbee3d;
    --card-dark: #2a2a2a;
    --card-light: #3a3a3a;
    --text-light: #f2f2f2;
    --page-bg: #d9d9d9;
  }
  * { box-sizing: border-box; margin: 0; padding: 0; }
  html, body { width: 1200px; height: 900px; overflow: hidden; }
  body {
    background: var(--page-bg);
    font-family: "Lato", sans-serif;
    position: relative;
  }
  .card {
    position: absolute;
    width: 560px;
    height: 320px;
    background: radial-gradient(ellipse at 45% 30%, var(--card-light) 0%, var(--card-dark) 70%);
    box-shadow: 0 8px 24px rgba(0,0,0,0.25);
  }
  .card--front { left: 560px; top: 70px; }
  .card--back { left: 80px; top: 480px; }

  .wordmark {
    display: flex;
    align-items: center;
    gap: 12px;
    color: var(--brand-yellow);
    font-weight: 700;
    letter-spacing: 0.5px;
  }
  .wordmark__dot {
    border-radius: 50%;
    background: var(--brand-red);
    flex-shrink: 0;
  }

  .card--front .wordmark {
    position: absolute;
    left: 0; right: 0; top: 110px;
    justify-content: center;
    font-size: 28px;
  }
  .card--front .wordmark__dot { width: 34px; height: 34px; }
  .front__web {
    position: absolute;
    left: 0; right: 0; top: 200px;
    text-align: center;
    color: var(--text-light);
    font-size: 15px;
    letter-spacing: 1px;
  }

  .card--back .wordmark {
    position: absolute;
    left: 26px; top: 140px;
    width: 210px;
    font-size: 17px;
    line-height: 1.25;
  }
  .card--back .wordmark__dot { width: 26px; height: 26px; }
  .back__divider {
    position: absolute;
    left: 258px; top: 60px;
    width: 1.5px; height: 200px;
    background: var(--brand-red);
  }
  .contact {
    position: absolute;
    left: 284px; top: 58px;
    color: var(--text-light);
    font-size: 15px;
    line-height: 1.4;
  }
  .contact__name {
    color: var(--brand-red);
    font-weight: 700;
    font-size: 21px;
    line-height: 1.2;
  }
  .contact__title { font-size: 15px; margin-bottom: 4px; }
  .contact__address { margin-bottom: 6px; }
  .contact__list { list-style: none; }
  .contact__item {
    display: flex;
    align-items: center;
    gap: 8px;
    font-size: 14.5px;
    line-height: 1.45;
  }
  .contact__icon { width: 13px; height: 13px; flex-shrink: 0; }
</style>
</head>
<body>

<section class="card card--front" aria-label="Card front">
  <div class="wordmark">
    <span class="wordmark__dot"></span>
    <span class="wordmark__name">Harbourline Supply Pty Ltd</span>
  </div>
  <p class="front__web">www.harbourlinesupply.com.au</p>
</section>

<section class="card card--back" aria-label="Card back">
  <div class="wordmark">
    <span class="wordmark__dot"></span>
    <span class="wordmark__name">Harbourline Supply Pty Ltd</span>
  </div>
  <div class="back__divider"></div>
  <div class="contact">
    <p class="contact__name">Vernon Ashcombe</p>
    <p class="contact__title">General Manager</p>
    <p class="contact__address">1450 Marlow Road<br>Alden TX 78010</p>
    <ul class="contact__list">
      <li class="contact__item">
        <svg class="contact__icon" viewBox="0 0 14 14" aria-hidden="true"><rect x="3.5" y="0.5" width="7" height="13" rx="1.5" fill="none" stroke="#ec1f27" stroke-width="1.4"/><circle cx="7" cy="11" r="0.9" fill="#ec1f27"/></svg>
        <span>0427 619 354</span>
      </li>
      <li class="contact__item">
        <svg class="contact__icon" viewBox="0 0 14 14" aria-hidden="true"><rect x="0.5" y="2.5" width="13" height="9" fill="#ec1f27"/><path d="M0.5 2.5 L7 8 L13.5 2.5" fill="none" stroke="#2a2a2a" stroke-width="1.2"/></svg>
        <span>vern@harbourlinesupply.com.au</span>
      </li>
      <li class="contact__item">
        <svg class="contact__icon" viewBox="0 0 14 14" aria-hidden="true"><rect x="0.5" y="2.5" width="13" height="9" fill="#ec1f27"/><path d="M0.5 2.5 L7 8 L13.5 2.5" fill="none" stroke="#2a2a2a" stroke-width="1.2"/></svg>
        <span>vern@coastwardgoods.com.au</span>
      </li>
      <li class="contact__item">
        <svg class="contact__icon" viewBox="0 0 14 14" aria-hidden="true"><circle cx="7" cy="7" r="6" fill="none" stroke="#ec1f27" stroke-width="1.4"/><ellipse cx="7" cy="7" rx="2.6" ry="6" fill="none" stroke="#ec1f27" stroke-width="1.1"/><line x1="1" y1="7" x2="13" y2="7" stroke="#ec1f27" stroke-width="1.1"/></svg>
        <span>www.harbourlinesupply.com.au</span>
      </li>
    </ul>
  </div>
</section>

</body>
</html>
```